We are a medial centre and have a 6m X3m window that we would like a medical image on it that is bright and has some colour on it. It can be abstract and like a feature wall . We don't want it to be dull. It can have some medical graphics but we want them to be subtle. The medical centre is the central hub. Our logo is included for your information but does not need to feature on the graphic

```html
<!DOCTYPE html>
<html lang="en">
<head>
<meta charset="utf-8">
<title>Harbourview Family Clinic – Window Banner</title>
<link href="https://fonts.googleapis.com/css2?family=Montserrat:wght@400;500;600&display=swap" rel="stylesheet">
<style>
  :root {
    --backdrop: #262626;
    --paper: #ffffff;
    --green: #6aaa3a;
    --teal: #0b7f7d;
    --ink: #1c2526;
    --photo-light: #f3f6f8;
    --photo-mid: #d9e3ea;
    --photo-blue: #a9cde3;
  }
  * { margin: 0; padding: 0; box-sizing: border-box; }
  html, body { width: 1200px; height: 1200px; overflow: hidden; }
  body { background: var(--backdrop); font-family: "Montserrat", sans-serif; position: relative; }

  .banner {
    position: absolute; left: 108px; top: 354px;
    width: 984px; height: 491px;
    background: var(--paper); overflow: hidden;
  }
  .banner__photo {
    position: absolute; left: 240px; top: 0; width: 744px; height: 380px;
    background:
      linear-gradient(90deg, var(--paper) 0%, rgba(255,255,255,0) 30%),
      radial-gradient(ellipse at 45% 45%, var(--photo-blue) 0%, rgba(169,205,227,0) 35%),
      linear-gradient(90deg, var(--photo-mid) 0%, var(--photo-light) 55%, #ffffff 75%, #e8ecef 100%);
  }
  .banner__waves { position: absolute; inset: 0; width: 984px; height: 491px; }

  .brand {
    position: absolute; left: 70px; top: 62px;
    color: var(--green); font-weight: 600; font-size: 38px;
    line-height: 1.15; letter-spacing: 1px;
  }

  .contact { position: absolute; left: 70px; top: 358px; list-style: none; color: var(--paper); }
  .contact__item { display: flex; align-items: center; gap: 14px; height: 36px; }
  .contact__item--phone { font-size: 32px; font-weight: 500; height: 42px; margin-bottom: 2px; }
  .contact__item--line { font-size: 17.5px; font-weight: 400; }
  .contact__icon { width: 30px; height: 30px; flex: none; }
</style>
</head>
<body>
  <section class="banner">
    <div class="banner__photo" role="img" aria-label="Photograph of a doctor in a white coat holding a stethoscope against a softly blurred bright clinic interior"></div>

    <svg class="banner__waves" viewBox="0 0 984 491" aria-hidden="true">
      <path d="M40,315 C220,250 420,262 600,350 C760,420 880,412 984,378 L984,491 L40,491 Z" fill="var(--teal)"/>
      <path d="M330,268 C520,250 700,340 820,350 C900,355 950,330 984,285 L984,380 C880,410 760,420 620,360 C520,310 430,275 330,268 Z" fill="var(--green)"/>
      <path d="M0,378 C70,320 170,296 262,304 C420,318 570,455 780,491 L0,491 Z" fill="var(--paper)"/>
      <path d="M0,388 C70,332 170,308 260,314 C420,326 560,470 760,491 L0,491 Z" fill="var(--ink)"/>
      <path d="M690,491 C830,470 910,455 984,430 L984,491 Z" fill="var(--paper)"/>
      <path d="M740,491 C860,475 930,462 984,442 L984,491 Z" fill="var(--ink)"/>
    </svg>

    <h1 class="brand">HARBOURVIEW<br>FAMILY CLINIC</h1>

    <ul class="contact">
      <li class="contact__item contact__item--phone">
        <svg class="contact__icon" viewBox="0 0 30 30"><circle cx="15" cy="15" r="15" fill="var(--green)"/><path d="M10.5,8.5 l2.5,-0.5 l1.5,3.5 l-1.8,1.2 c0.8,1.8 2,3 3.6,3.6 l1.2,-1.8 l3.5,1.5 l-0.5,2.5 c-6,0.5 -10.5,-4 -10,-10 z" fill="#fff"/></svg>
        0198765432
      </li>
      <li class="contact__item contact__item--line">
        <svg class="contact__icon" viewBox="0 0 30 30"><circle cx="15" cy="15" r="15" fill="var(--green)"/><rect x="8.5" y="10" width="13" height="10" rx="1" fill="#fff"/><path d="M8.5,10.5 L15,15.5 L21.5,10.5" fill="none" stroke="var(--green)" stroke-width="1.3"/></svg>
        info@harbourviewclinic.com
      </li>
      <li class="contact__item contact__item--line">
        <svg class="contact__icon" viewBox="0 0 30 30"><circle cx="15" cy="15" r="15" fill="var(--green)"/><path d="M15,7 a5.5,5.5 0 0 1 5.5,5.5 c0,4 -5.5,10 -5.5,10 c0,0 -5.5,-6 -5.5,-10 a5.5,5.5 0 0 1 5.5,-5.5 z" fill="#fff"/><circle cx="15" cy="12.5" r="2" fill="var(--green)"/></svg>
        www.harbourviewclinic.com
      </li>
    </ul>
  </section>
</body>
</html>
```